Home Based Business Website Design

Need 1 template web design. Require clean friendly website design that helps promote a work from home business opportunity based around personal development. The site should lean towards appealing to the female market (see target market) and be straight forward, fresh colours and good use of white space. The site should have a family focus using imagery of happy families and reinforcing the quality of life and freedom available. The site should be in a two or three column format, navigation can be top or left, there will be 6 menu items in total (E.g. home, about, testimonials, contact, faq, why me?). There should be space for a video, text, images and a clear "call to action" (contact us). The site should come across as professiona, positive, friendly and trustworthy. Scope for many more sites of this nature in the future.

Target Market(s)

People that are ready for change. People wanting to make money from a business at home. 25+ years old, mum's , professional. People that are tired of the commute and want a better quality of life. While the site should lean towards focusing on stay at home mums or working mums looking for a better life it should also be able to appeal to a wider audience (male and female) so should not be too "girly"!

Industry/Entity Type

Business

Requirements
Must have
• Fairly open to interpretation, site must have at least two columns, clear call to action, space for a video, text and images, navigation (single level 6 items).
Nice to have
• Possibly animated banner of images?
Should not have
• Try to use less obvious imagery no stressed out executives or people jumping for joy. no dark designs no purple or flouro colours. Site should be modern in design.

```html
<!DOCTYPE html>
<html lang="en">
<head>
<meta charset="utf-8">
<title>Work at Home</title>
<link href="https://fonts.googleapis.com/css2?family=Arimo:wght@400;700&family=Gochi+Hand&display=swap" rel="stylesheet">
<style>
:root{
  --page:#ffb66e;
  --orange:#f56400;
  --orange-mid:#f77b12;
  --orange-light:#f98f22;
  --gold:#ffd34a;
  --phone:#ffd95c;
  --cream:#fff8e7;
  --ink:#333333;
  --grey:#f6f6f6;
  --white:#ffffff;
}
*{margin:0;padding:0;box-sizing:border-box}
html,body{width:1200px;height:1150px;overflow:hidden}
body{background:var(--page);font-family:Arimo,Arial,sans-serif;position:relative;color:var(--ink)}
.abs{position:absolute}
.hand{font-family:"Gochi Hand",cursive}

.site-header{left:120px;top:105px;width:961px;height:125px;background:var(--orange);border-top-right-radius:18px;overflow:hidden}
.site-header svg{position:absolute;right:0;top:0}
.header-ornament{left:0;top:0;width:230px;height:95px;background:linear-gradient(90deg,rgba(255,170,90,.45),rgba(245,100,0,0))}
.brand{left:40px;top:44px;font-size:34px;font-weight:400;color:#ffc21a;letter-spacing:1px}
.phone{right:13px;top:30px;font-size:22px;font-weight:700;color:var(--phone);display:flex;align-items:center;gap:6px;letter-spacing:.5px}
.cta-line{right:13px;top:64px;font-size:25px;color:var(--white)}

.main-nav{left:120px;top:230px;width:961px;height:38px;background:var(--orange-mid)}
.main-nav a{position:absolute;top:11px;font-size:14px;color:var(--white);text-decoration:none}
.main-nav .active{left:5px;top:7px;width:80px;height:24px;background:var(--orange);border-radius:12px;text-align:center;line-height:24px}
.register{position:absolute;right:0;top:0;width:192px;height:38px;background:linear-gradient(#ffffff,#e6e6e6);text-align:center;font-size:24px;color:var(--orange);line-height:38px}

.content{left:120px;top:278px;width:677px;height:727px;background:var(--white)}
.feature{left:0;top:0;width:677px;height:310px;background:var(--cream)}
.photo-strip{left:29px;top:15px;width:411px;height:39px;background:linear-gradient(90deg,#ecebe6,#f7f6f2,#e8e7e2)}
.photo{left:47px;top:36px;width:387px;height:244px;background:linear-gradient(135deg,#e9efe2,#f3ede6 45%,#d8c6b3);box-shadow:0 2px 6px rgba(0,0,0,.25)}
.photo-name{left:47px;top:235px;width:189px;height:26px;background:var(--orange-mid);color:var(--white);font-size:20px;padding-left:24px;line-height:26px}
.quote-mark{font-family:Georgia,serif;font-size:110px;font-weight:700;color:var(--orange-light);line-height:1}
.quote-text{left:445px;top:87px;width:214px;text-align:center;font-size:22px;line-height:24px;color:var(--orange)}

.intro{left:37px;top:355px;width:602px;height:327px;background:var(--cream);padding:22px 27px}
.intro h1{font-weight:400;font-size:25px;color:var(--orange);margin-bottom:22px}
.intro p{font-size:12px;line-height:23.5px;color:var(--ink);margin-bottom:24px}

.video-panel{left:807px;top:278px;width:274px;height:310px;background:var(--gold)}
.video{left:18px;top:27px;width:240px;height:196px;background:linear-gradient(#8a8a7c,#b2ad9d 50%,#55534c);overflow:hidden}
.video-bar{left:0;bottom:0;width:240px;height:14px;background:#1e2430}
.play{left:101px;top:72px;width:38px;height:38px;border-radius:50%;background:rgba(255,255,255,.55)}
.play-label{left:96px;top:108px;font-size:9px;color:var(--white)}
.more-videos{left:23px;top:248px;width:232px;height:42px;border-radius:21px;background:linear-gradient(#ffffff,#e4e4e4);text-align:center;line-height:42px;font-size:22px;color:var(--orange)}

.works{left:807px;top:599px;width:274px;height:353px;background:var(--white)}
.works h2{position:absolute;left:0;top:17px;width:274px;text-align:center;font-weight:400;font-size:20px;color:var(--orange)}
.work-item{left:26px;width:217px;height:77px;background:var(--grey);padding:13px 13px}
.work-item a{font-size:13px;line-height:15.5px;color:#111;text-decoration:underline}
.view-more{right:31px;top:328px;font-size:11px;color:#333;text-decoration:underline}

.side-footer-band{left:807px;top:963px;width:274px;height:42px;background:var(--gold)}

.site-footer{left:120px;top:1017px;width:961px;height:31px;background:var(--orange);color:var(--white);font-size:11px}
.site-footer .copy{position:absolute;left:33px;top:10px}
.site-footer nav{position:absolute;right:10px;top:10px}
.site-footer a{color:var(--white);text-decoration:none;margin:0 5px}
</style>
</head>
<body>

<header class="site-header abs">
  <svg width="420" height="125" viewBox="0 0 420 125" aria-hidden="true">
    <path d="M0 125 C180 110 330 70 420 10 L420 125 Z" fill="var(--orange-light)" opacity=".85"/>
    <path d="M170 125 C280 100 370 60 420 20 L420 125 Z" fill="#fb9a2c" opacity=".6"/>
  </svg>
  <div class="header-ornament abs" role="img" aria-label="Floral scroll ornament"></div>
  <div class="brand abs">WORK AT HOME</div>
  <div class="phone abs">
    <svg width="14" height="14" viewBox="0 0 24 24" aria-hidden="true"><path fill="var(--phone)" d="M6.6 10.8a15 15 0 0 0 6.6 6.6l2.2-2.2c.3-.3.7-.4 1-.2 1.1.4 2.3.6 3.6.6.6 0 1 .4 1 1V20c0 .6-.4 1-1 1A17 17 0 0 1 3 4c0-.6.4-1 1-1h3.5c.6 0 1 .4 1 1 0 1.3.2 2.5.6 3.6.1.3 0 .7-.2 1z"/></svg>
    <span>1300 480 XXX</span>
  </div>
  <div class="cta-line abs hand">call to action</div>
</header>

<nav class="main-nav abs">
  <a class="active" href="#">HOME</a>
  <a href="#" style="left:137px">ABOUT US</a>
  <a href="#" style="left:277px">TESTIMONIALS</a>
  <a href="#" style="left:441px">CONTACT</a>
  <a href="#" style="left:572px">FAQ</a>
  <a href="#" style="left:675px">WHY ME ?</a>
  <a class="register hand" href="#">Register HERE</a>
</nav>

<main class="content abs">
  <section class="feature abs">
    <div class="photo-strip abs" role="img" aria-label="Faint lace pattern strip"></div>
    <div class="photo abs" role="img" aria-label="Happy family of mother, father and daughter at home"></div>
    <div class="photo-name abs hand">Clara Bennett</div>
    <div class="quote-mark abs" style="left:456px;top:22px">&ldquo;</div>
    <p class="quote-text abs hand">Lorem ipsum do or sit amet, consec tur adipiscing elit. uis non convalli gula.</p>
    <div class="quote-mark abs" style="left:620px;top:225px">&rdquo;</div>
  </section>

  <article class="intro abs">
    <h1>Work at home OPPORTUNITIES !!</h1>
    <p>Lorem ipsum dolor sit amet, consectetur adipiscing elit. Duis non convallis ligula. Aenean quis justo ipsum, quis aliquet purus. Proin sodales magna quis augue aliquet eu sollicitudin lectus sodales. Morbi eu tristique eros. Sed felis metus, mollis eget ornare ut, auctor et sem. Morbi gravida porta felis id dapibus. Maecenas semper neque vel arcu blandit tristique. Curabitur vulputate quam a massa laoreet id mollis sem male-suada. Pellentesque habitant morbi tristique senectus et netus et malesuada fames ac turpis egestas. Proin a pulvinar metus.</p>
    <p>Proin rhoncus elementum metus, ac vestibulum turpis tincidunt eget. Nunc condimentum rutrum felis, id fermentum nibh lobortis ac. Vestibulum eu quam id leo bibendum fringilla vehicula sit amet odio. Morbi nec laoreet sapien. Morbi facilisis ele</p>
  </article>
</main>

<aside class="video-panel abs">
  <div class="video abs" role="img" aria-label="Video of a woman talking about working from home">
    <div class="play abs"></div>
    <svg class="abs" style="left:114px;top:83px" width="14" height="16" viewBox="0 0 14 16" aria-hidden="true"><path d="M2 1 L13 8 L2 15 Z" fill="#8a8a8a"/></svg>
    <span class="play-label abs">Play Video</span>
    <div class="video-bar abs"></div>
  </div>
  <div class="more-videos abs hand">Watch More Videos</div>
</aside>

<aside class="works abs">
  <h2>Recent Top 3 Works</h2>
  <div class="work-item abs" style="top:59px"><a href="#">Lorem ipsum dolor sit amet, cons ectetur adipiscing elit. Duis non ligula. Aenean quis ju</a></div>
  <div class="work-item abs" style="top:148px"><a href="#">Lorem ipsum dolor sit amet, cons ectetur adipiscing elit. Duis non ligula. Aenean quis ju</a></div>
  <div class="work-item abs" style="top:238px"><a href="#">Lorem ipsum dolor sit amet, cons ectetur adipiscing elit. Duis non ligula. Aenean quis ju</a></div>
  <a class="view-more abs" href="#">view more works</a>
</aside>

<div class="side-footer-band abs"></div>

<footer class="site-footer abs">
  <span class="copy">Copyright 2009. WORK AT HOME</span>
  <nav>| <a href="#">Home</a>| <a href="#">Privacy Policy</a>| <a href="#">Faq</a>| <a href="#">Contact</a>|</nav>
</footer>

</body>
</html>
```